WP website design (Brenmoor)

We need a wordpress design for an established auction and real estate company based in Kentucky. The winning design will incorporate a professional color scheme with company logo in a clean layout with specified widgets. The design needs to consider that this will be developed on a responsive theme. Color is #307d84, with gray/black or other as an accent/highlight color.

Industry/Entity Type

Real Estate

Requirements
Must have
• Elelments of design need to consider that this site is going to be developed on a responsive theme.

Navigation:
1) Home 2) Current Auctions 3) Past Auctions 4) Meet the Staff 5) For Sellers 6) For Buyers 7) Testimonials 8) Contact Us

Colors will be the blue of logo plus black/gray or other accent color.

Slideshow will be prominent, please use stock real estate photo for initial image. Will have following in either header or sidebar: testimonials, social icons (FB, linkedin Twitter, RSS), Featured Auctions widget, newsletter signup form.

Footer will have contact info (below) and attached affiliation logos.
Brenmoor Auctions, Inc.
8415 Tamsen Rd., Louisville KY 40291
glen.office@brenmoorbid.example
Phone: (502) 736 2048

```html
<!DOCTYPE html>
<html lang="en">
<head>
<meta charset="utf-8">
<title>Brenmoor Auctions, Inc.</title>
<link href="https://fonts.googleapis.com/css2?family=Asap:wght@400;500;600&family=Arimo:wght@400;700&display=swap" rel="stylesheet">
<style>
:root{
  --teal:#0d8186;
  --orange:#f9a91a;
  --ink:#1a1a1a;
  --body:#333;
  --line:#d9d9d9;
  --panel:#ebebeb;
  --band:#efefef;
  --white:#fff;
  --sep:rgba(255,255,255,.55);
}
*{box-sizing:border-box;margin:0;padding:0}
html,body{width:920px;height:1200px;overflow:hidden;background:var(--white)}
body{position:relative;font-family:"Arimo",Arial,sans-serif;color:var(--body)}
.abs{position:absolute}

/* header */
.brand{left:76px;top:24px;display:flex;align-items:center;gap:8px}
.brand-mark{width:20px;height:20px;background:var(--teal)}
.brand-name{font-family:"Asap",sans-serif;font-weight:600;font-size:22px;color:var(--teal);letter-spacing:.5px;text-transform:uppercase}
.social{right:83px;top:50px;display:flex;gap:6px}
.social span{width:30px;height:30px;background:#2a2a2a;display:block}

/* nav */
.nav{left:0;top:88px;width:920px;height:42px;background:linear-gradient(#fbb42a,var(--orange));border-bottom:1px solid #e89a0c}
.nav-item{top:0;height:42px;line-height:44px;font-family:"Asap",sans-serif;font-weight:500;font-size:11.5px;color:var(--ink);text-transform:uppercase;white-space:nowrap}
.nav-sep{top:8px;height:26px;border-left:1px solid var(--sep)}
.nav-item.active{left:466px;width:88px;height:44px;text-align:center;background:var(--teal);color:var(--white)}
.nav-item.active::before{content:"";position:absolute;left:50%;bottom:6px;margin-left:-4px;border:4px solid transparent;border-top:5px solid var(--ink)}
.nav-home{left:88px;top:13px}

/* slider */
.slide{left:76px;top:132px;width:554px;height:290px;background:linear-gradient(180deg,#6b8f5a 0%,#d9cfb0 35%,#cfc6ad 55%,#3f7f84 80%,#2d6b70 100%)}
.dropdown{left:466px;top:132px;width:94px;height:138px;background:var(--teal);padding-top:2px}
.dropdown a{display:block;margin:0 3px 0 10px;height:26.5px;padding-top:9px;border-bottom:1px solid rgba(255,255,255,.35);color:var(--white);font-family:"Asap",sans-serif;font-size:9px;text-decoration:none;text-transform:uppercase}
.dropdown a:last-child{border-bottom:0}
.feature{left:635px;width:208px;height:70px}
.feature h4{position:absolute;left:7px;top:3px;width:136px;font-family:"Asap",sans-serif;font-weight:500;font-size:11px;color:var(--ink);border-bottom:2px solid var(--ink);padding-bottom:2px}
.feature p{position:absolute;left:8px;top:22px;width:136px;font-size:9px;line-height:12px;color:#555;text-align:justify}
.feature .thumb{position:absolute;right:2px;top:3px;width:54px;height:60px;border:2px solid var(--orange);border-radius:4px;background:linear-gradient(#9fbfd8,#d6ccae 55%,#6c9450)}
.feature.current{background:var(--orange)}
.feature.current::before{content:"";position:absolute;left:-36px;top:0;border:35px solid transparent;border-right:36px solid var(--orange);border-left:0}
.feature.current h4,.feature.current p{color:var(--ink)}
.feature.current .thumb{border-color:var(--white)}

/* auctions */
.section-title{left:76px;top:442px;font-family:"Asap",sans-serif;font-weight:500;font-size:17px;color:var(--teal);text-transform:uppercase;display:flex;align-items:center;gap:6px}
.card{left:76px;width:550px;height:155px;border:1px solid var(--line)}
.card .band{position:absolute;left:4px;top:6px;width:540px;height:29px;background:var(--band);padding-left:45px;line-height:29px;font-family:"Asap",sans-serif;font-size:12px;color:var(--orange);text-transform:uppercase}
.card .photo{position:absolute;left:5px;top:41px;width:150px;height:88px;border:2px solid #ccc;background:linear-gradient(#8db4d6 0%,#b9cbd8 35%,#9a8a6a 50%,#5e9a3c 60%,#4f8a2f 100%)}
.card .btns{position:absolute;left:4px;top:134px;display:flex;gap:4px}
.card .btns span{background:#111;color:var(--white);font-family:"Asap",sans-serif;font-size:9px;padding:3px 5px;text-transform:uppercase}
.card .btns span.on{color:var(--orange)}
.card .info{position:absolute;left:164px;top:48px;width:382px;font-size:9.5px;color:#333}
.card .info h3{font-family:"Asap",sans-serif;font-weight:500;font-size:12px;color:var(--teal);text-transform:uppercase;margin-bottom:7px}
.card .row{display:flex;margin-bottom:6px;line-height:14px}
.card .row b{font-family:"Asap",sans-serif;font-weight:600;color:var(--ink);white-space:nowrap;margin-right:4px}
.card .row p{text-align:justify}

/* sidebar */
.sidebar{left:643px;top:434px;width:200px;height:584px;background:var(--panel)}
.side-h{font-family:"Asap",sans-serif;font-weight:500;font-size:12px;color:var(--teal);text-transform:uppercase}
.side-p{font-size:9px;line-height:13px;color:#333}
.signup-input{left:656px;top:498px;width:176px;height:25px;background:var(--white);border:1px solid #ddd}
.subscribe{left:777px;top:532px;background:#111;color:var(--white);font-family:"Asap",sans-serif;font-size:9.5px;padding:5px 5px}
.rule{left:652px;width:184px;border-top:1px solid #d0d0d0}
.news-photo{width:44px;height:52px;border:2px solid var(--orange);background:linear-gradient(#8d6a55,#c59f88)}
.news-text{width:124px;font-size:8.5px;line-height:13.5px;color:#333}
.news-text a{color:var(--orange);text-decoration:none}
.scroll{left:829px;top:591px;width:6px;height:158px;background:var(--white);border-radius:3px}
.scroll::after{content:"";position:absolute;left:0;top:28px;width:6px;height:20px;border-radius:3px;background:#555}
.quote{left:660px;width:172px;font-size:9.5px;line-height:14px;color:#333;text-align:justify;padding:0 2px 6px 6px;border-left:1px solid #cfcfcf;border-bottom:1px solid #cfcfcf}
.quote .mark{display:inline-block;height:12px;font-family:Georgia,serif;font-size:22px;line-height:20px;color:#c8c8c8;vertical-align:top;margin:0 2px}
.quote-by{left:657px;font-size:8px;font-style:italic;font-weight:700;color:#7ea44a}

/* footer */
.footer{left:0;top:1048px;width:920px;height:114px;background:var(--teal)}
.map{left:78px;top:1070px;width:119px;height:75px;background:linear-gradient(135deg,#eef0e8,#d8dec9);border:2px solid var(--white)}
.contact{left:204px;top:1068px;color:var(--white);font-family:"Asap",sans-serif;text-transform:uppercase}
.contact h5{font-weight:400;font-size:14px;color:var(--ink);margin-bottom:4px}
.contact .co{font-size:12.5px;margin-bottom:2px}
.contact p{font-size:9.5px;line-height:14px}
.contact .ph{color:var(--orange)}
.badges{left:573px;top:1085px;display:flex;align-items:center;gap:12px}
.badges span{display:block;background:#1c2a2c}
.copy{left:0;top:1162px;width:920px;height:38px;background:#0b0b0b;color:var(--white);font-size:9px;text-align:center;line-height:38px}
</style>
</head>
<body>

<header>
  <div class="abs brand"><span class="brand-mark"></span><span class="brand-name">Brenmoor Auctions Inc.</span></div>
  <div class="abs social" aria-label="Social links"><span></span><span></span><span></span><span></span></div>
</header>

<nav class="abs nav">
  <svg class="abs nav-home" width="16" height="14" viewBox="0 0 16 14" aria-label="Home"><path d="M8 0 0 7h2v7h4V9h4v5h4V7h2z" fill="#1a1a1a"/></svg>
  <span class="abs nav-sep" style="left:117px"></span>
  <span class="abs nav-item" style="left:129px">Current Auctions</span>
  <span class="abs nav-sep" style="left:248px"></span>
  <span class="abs nav-item" style="left:259px">Past Auctions</span>
  <span class="abs nav-sep" style="left:354px"></span>
  <span class="abs nav-item" style="left:366px">Meet the Staff</span>
  <span class="abs nav-item active">For Sellers</span>
  <span class="abs nav-item" style="left:568px">For Buyers</span>
  <span class="abs nav-sep" style="left:645px"></span>
  <span class="abs nav-item" style="left:657px">Testimonials</span>
  <span class="abs nav-sep" style="left:740px"></span>
  <span class="abs nav-item" style="left:753px">Contact Us</span>
</nav>

<div class="abs slide" role="img" aria-label="Stock photo of a cream villa with a pool and lounge chairs"></div>
<div class="abs dropdown">
  <a href="#">Demo Link 1</a><a href="#">Demo Link 2</a><a href="#">Demo Link 3</a><a href="#">Demo Link 4</a><a href="#">Demo Link 5</a>
</div>

<div class="abs feature" style="top:136px"><h4>LOREM IPSUM DOLOR SIT</h4><p>Lorem Ipsum is simply dummy text of the printing and typesetting industry.</p><div class="thumb" role="img" aria-label="House photo"></div></div>
<div class="abs feature current" style="top:206px"><h4>LOREM IPSUM DOLOR SIT</h4><p>Lorem Ipsum is simply dummy text of the printing and typesetting industry.</p><div class="thumb" role="img" aria-label="Pool photo"></div></div>
<div class="abs feature" style="top:284px"><h4>LOREM IPSUM DOLOR SIT</h4><p>Lorem Ipsum is simply dummy text of the printing and typesetting industry.</p><div class="thumb" role="img" aria-label="Poolside photo"></div></div>
<div class="abs feature" style="top:356px"><h4>LOREM IPSUM DOLOR SIT</h4><p>Lorem Ipsum is simply dummy text of the printing and typesetting industry.</p><div class="thumb" role="img" aria-label="House photo"></div></div>

<h2 class="abs section-title"><svg width="13" height="12" viewBox="0 0 13 12"><path d="M0 0h3l4 6-4 6H0l4-6zM6 0h3l4 6-4 6H6l4-6z" fill="#0d8186"/></svg>Current Auctions</h2>

<section>
  <article class="abs card" style="top:476px">
    <div class="band">Live On-Side Auction with Online Bidding</div>
    <div class="photo" role="img" aria-label="Photo of a large shingle house on a lawn"></div>
    <div class="btns"><span>Live Video</span><span class="on">Details</span></div>
    <div class="info">
      <h3>Live On-Side Auction</h3>
      <div class="row"><b>DATE :</b><span>Sunday, July 06, 2014 at 09:00 AM</span></div>
      <div class="row"><b>LOCATIONS :</b><span>8415 Tamsen Rd., Louisville KY 40291</span></div>
      <div class="row"><b>DETAIL :</b><p>Lorem ipsum dolor sit amet, consectetuer adipiscing elit. Aenean commodo ligula eget dolor. Aenean massa. Cum sociis natoque penatibus et magnis dis parturient montes,</p></div>
    </div>
  </article>
  <article class="abs card" style="top:668px">
    <div class="band">Live On-Side Auction with Online Bidding</div>
    <div class="photo" role="img" aria-label="Photo of a large shingle house on a lawn"></div>
    <div class="btns"><span>Live Video</span><span>Details</span></div>
    <div class="info">
      <h3>Live On-Side Auction</h3>
      <div class="row"><b>DATE :</b><span>Sunday, July 06, 2014 at 09:00 AM</span></div>
      <div class="row"><b>LOCATIONS :</b><span>8415 Tamsen Rd., Louisville KY 40291</span></div>
      <div class="row"><b>DETAIL :</b><p>Lorem ipsum dolor sit amet, consectetuer adipiscing elit. Aenean commodo ligula eget dolor. Aenean massa. Cum sociis natoque penatibus et magnis dis parturient montes,</p></div>
    </div>
  </article>
  <article class="abs card" style="top:864px">
    <div class="band">Live On-Side Auction with Online Bidding</div>
    <div class="photo" role="img" aria-label="Photo of a large shingle house on a lawn"></div>
    <div class="btns"><span>Live Video</span><span>Details</span></div>
    <div class="info">
      <h3>Live On-Side Auction</h3>
      <div class="row"><b>DATE :</b><span>Sunday, July 06, 2014 at 09:00 AM</span></div>
      <div class="row"><b>LOCATIONS :</b><span>8415 Tamsen Rd., Louisville KY 40291</span></div>
      <div class="row"><b>DETAIL :</b><p>Lorem ipsum dolor sit amet, consectetuer adipiscing elit. Aenean commodo ligula eget dolor. Aenean massa. Cum sociis natoque penatibus et magnis dis parturient montes,</p></div>
    </div>
  </article>
</section>

<aside>
  <div class="abs sidebar"></div>
  <h3 class="abs side-h" style="left:656px;top:448px">Email Sign-Up</h3>
  <p class="abs side-p" style="left:656px;top:465px;width:180px">Sign up for our free messages &amp; Auctions alerts</p>
  <div class="abs signup-input"></div>
  <span class="abs subscribe">SUBSCRIBE</span>
  <div class="abs rule" style="top:565px"></div>

  <h3 class="abs side-h" style="left:656px;top:586px">News &amp; Events</h3>
  <div class="abs news-photo" style="left:657px;top:609px" role="img" aria-label="Staff portrait"></div>
  <p class="abs news-text" style="left:705px;top:607px">Lorem ipsum dolor sit amet, con adipiscing elit. Aenean commod ligula eget dolor.<br><a href="#">Read More...</a></p>
  <div class="abs news-photo" style="left:657px;top:686px" role="img" aria-label="Staff portrait"></div>
  <p class="abs news-text" style="left:705px;top:684px">Lorem ipsum dolor sit amet, con adipiscing elit. Aenean commod ligula eget dolor.<br><a href="#">Read More...</a></p>
  <div class="abs scroll"></div>
  <div class="abs rule" style="top:765px"></div>

  <h3 class="abs side-h" style="left:656px;top:780px">Testimonials</h3>
  <blockquote class="abs quote" style="top:806px"><span class="mark">&ldquo;</span>Lorem ipsum dolor sit amet, consectetuer adipiscing elit. Aenean commodo ligula eget dolor. Aenean massa. Cum sociis natoque penatibus et magnis dis parturient montes,<span class="mark">&rdquo;</span></blockquote>
  <span class="abs quote-by" style="top:900px">Dana Whitfield</span>
  <blockquote class="abs quote" style="top:932px"><span class="mark">&ldquo;</span>Lorem ipsum dolor sit amet, consectetuer adipiscing elit. Aenean commodo turient montes,<span class="mark">&rdquo;</span></blockquote>
  <span class="abs quote-by" style="top:996px">Dana Whitfield</span>
</aside>

<footer>
  <div class="abs footer"></div>
  <div class="abs map" role="img" aria-label="Map to the office"></div>
  <div class="abs contact">
    <h5>Contact Us</h5>
    <div class="co">Brenmoor Auctions, Inc.</div>
    <p>8415 Tamsen Rd., Louisville KY 40291</p>
    <p>glen.office@brenmoorbid.example</p>
    <p>Phone: <span class="ph">(502) 736 2048</span></p>
  </div>
  <div class="abs badges" aria-label="Affiliations">
    <span style="width:86px;height:40px;border-radius:50%"></span>
    <span style="width:38px;height:40px"></span>
    <span style="width:30px;height:44px"></span>
    <span style="width:40px;height:36px"></span>
    <span style="width:36px;height:40px"></span>
  </div>
  <div class="abs copy">Copyright @ 2014-Brenmoor Auctions, Inc.- All Rights Reserved.</div>
</footer>

</body>
</html>
```